Label Redesign For Hemp Oil Tincture Bottle*

I need a label redesigned for Meadowlark Botanics, current bottle label and logo is attached. The current label doesn't standout, not sure if its the font size or colors on the existing label. It is very important to have on the label that this is a Premium Full Spectrum Hemp Oil that is 2000mg. Then after the label is redesigned and approved, I would need to packaging to be designed to match the approved label design.
This Hemp oil has a relaxing effect to help ease mental and emotional stress, tension and worry. The Omega Fatty Acids it contains also naturally improves your mood and overall brain function, causing you to feel more alert and focused. Hemp Oil helps with insomnia. Take some 2-3 hours before bedtime, you will feel relaxed yet aware of how tired you are that it will lead to a good night's sleep. Hemp Oil helps ease chronic pain and inflammation from conditions such as arthritis, fibromyalgia, lupus, and MS. As a pain relief supplement, it is a safer, natural, non-chemical and non-addictive alternative to prescription painkillers.
Updates

Target Market(s)

Adults

Industry/Entity Type

Supplement

Font styles to use
Serif
Sans Serif

Colors

Designer to choose colors to be used in the design.

Requirements
Must have
• All information thats on current label but where it says 750 in the front of the existing label, it needs to say 2000. The 2000 should be prominent on the label.

```html
<!DOCTYPE html>
<html lang="en">
<head>
<meta charset="utf-8">
<title>Meadowlark Botanics – Full Spectrum Hemp Oil Label</title>
<link href="https://fonts.googleapis.com/css2?family=Oswald:wght@400;500;600&family=Montserrat:wght@600&family=Great+Vibes&display=swap" rel="stylesheet">
<style>
  :root {
    --canvas-bg: #c9ccd0;
    --panel-white: #f1f1f2;
    --panel-wave: #e3e3e6;
    --brand-pink: #c8205d;
    --band-pink: #d0266a;
    --band-deep: #8d1a3c;
    --leaf-green: #a8c98a;
    --mark-grey: #6f7072;
    --white: #ffffff;
  }
  * { margin: 0; padding: 0; box-sizing: border-box; }
  html, body { width: 1200px; height: 1200px; overflow: hidden; }
  body {
    background: linear-gradient(180deg, #b9bcc1 0%, var(--canvas-bg) 55%, #e4e5e7 100%);
    position: relative;
    font-family: "Oswald", sans-serif;
  }
  .label {
    position: absolute;
    left: 405px; top: 60px;
    width: 390px; height: 1080px;
    overflow: hidden;
    background: var(--panel-white);
  }
  .label__texture {
    position: absolute; left: 0; top: 0; width: 390px; height: 630px;
    background: linear-gradient(160deg, var(--panel-white) 0%, var(--panel-wave) 50%, var(--panel-white) 100%);
  }
  .label__band {
    position: absolute; left: 0; top: 630px; width: 390px; height: 450px;
    background: linear-gradient(100deg, var(--band-pink) 0%, #b61f52 50%, var(--band-deep) 100%);
  }
  .badge-thc {
    position: absolute; left: 25px; top: 2px; width: 125px; height: 73px;
    background: linear-gradient(90deg, var(--brand-pink), #9c1d42);
    color: var(--white);
    font-weight: 500; font-size: 31px; line-height: 30px;
    text-align: center; padding-top: 6px;
  }
  .vertical {
    position: absolute;
    writing-mode: vertical-rl;
    transform: rotate(180deg);
    white-space: nowrap;
  }
  .brand-name {
    left: 50px; bottom: 470px;
    font-weight: 500; font-size: 46px; line-height: 52px;
    letter-spacing: 0.5px; color: var(--brand-pink);
  }
  .premium {
    left: 118px; bottom: 470px;
    font-family: "Great Vibes", cursive;
    font-size: 60px; line-height: 56px; color: var(--brand-pink);
  }
  .brand-mark {
    position: absolute; left: 150px; top: 190px; width: 220px;
    text-align: center;
  }
  .brand-mark__dot {
    width: 90px; height: 90px; border-radius: 50%;
    background: var(--leaf-green); margin: 0 auto 14px;
  }
  .brand-mark__name {
    font-weight: 500; font-size: 23px; color: var(--mark-grey);
    letter-spacing: 0.5px; white-space: nowrap;
  }
  .strength {
    position: absolute; right: 30px; top: 538px;
    text-align: center; color: var(--brand-pink);
  }
  .strength__type { font-size: 26px; font-weight: 500; line-height: 30px; letter-spacing: 0.3px; white-space: nowrap; }
  .strength__amount {
    display: inline-block;
    margin-top: 4px; border: 3px solid var(--brand-pink);
    padding: 0 6px;
    font-size: 27px; font-weight: 500; line-height: 31px;
    white-space: nowrap;
  }
  .supplement {
    left: 50px; bottom: 25px;
    font-weight: 500; font-size: 46px; line-height: 46px; color: var(--white);
  }
  .benefits {
    position: absolute; right: 40px; top: 682px; width: 200px;
  }
  .divider {
    position: relative; height: 12px;
  }
  .divider::before {
    content: ""; position: absolute; left: 0; right: 0; top: 6px;
    border-top: 1px solid rgba(255,255,255,0.8);
  }
  .divider::after {
    content: ""; position: absolute; left: 50%; top: 1px;
    width: 8px; height: 8px; margin-left: -4px;
    border: 1px solid var(--white); background: var(--band-pink);
    transform: rotate(45deg);
  }
  .benefits__text {
    font-family: "Montserrat", sans-serif; font-weight: 600;
    font-size: 18px; line-height: 22.5px; color: var(--white);
    text-align: right; margin: 6px 0 6px; white-space: nowrap;
  }
  .natural {
    position: absolute; right: 40px; top: 796px;
    font-family: "Great Vibes", cursive; font-size: 42px; color: var(--white);
  }
  .flavor {
    position: absolute; right: 40px; top: 846px;
    font-family: "Montserrat", sans-serif; font-weight: 600;
    font-size: 19px; color: var(--white);
  }
  .volume {
    position: absolute; right: 40px; top: 1038px;
    font-size: 18px; font-weight: 500; color: var(--white); letter-spacing: 0.5px;
  }
</style>
</head>
<body>
  <main class="label">
    <div class="label__texture" role="img" aria-label="Soft grey wavy line texture on the white panel"></div>
    <div class="label__band" role="img" aria-label="Pink to crimson band with flowing wavy line texture"></div>

    <div class="badge-thc">ZERO<br>THC</div>

    <h1 class="vertical brand-name">MEADOWLARK BOTANICS</h1>
    <div class="vertical premium">premium</div>

    <div class="brand-mark">
      <div class="brand-mark__dot"></div>
      <div class="brand-mark__name">Meadowlark Botanics</div>
    </div>

    <div class="strength">
      <div class="strength__type">FULL SPECTRUM</div>
      <div class="strength__amount">2000 HEMP OIL</div>
    </div>

    <div class="vertical supplement">DIETARY SUPPLEMENT</div>

    <section class="benefits">
      <div class="divider"></div>
      <p class="benefits__text">Pain,sleeplessness<br>anxiety &amp;<br>inflammation</p>
      <div class="divider"></div>
    </section>

    <div class="natural">Natural</div>
    <div class="flavor">Peppermint Flavor</div>
    <div class="volume">1FL.OZ (30ML)</div>
  </main>
</body>
</html>
```